Sales Flyer Design

Create a Flyer front and back that highlights the different things we do
We do Addition, basements, kitchens, bathrooms, concrete, siding, Roofing.

We want to highlight that we are licensed Electrical Contractor and Plumbers.
Use our Logo attached keeping color scheme mainly our company colors. We are looking for an attention grabbing but easy read for homeowners.

```html
<!DOCTYPE html>
<html lang="en">
<head>
<meta charset="utf-8">
<title>Hartwell Remodeling &amp; Restoration – Flyer</title>
<link href="https://fonts.googleapis.com/css2?family=Montserrat:wght@400;500;700;800&family=Oswald:wght@600;700&display=swap" rel="stylesheet">
<style>
  :root{
    --orange:#e8622c;
    --dark:#231f20;
    --white:#ffffff;
    --bg:#8a8a8a;
    --text:#2b2b2b;
  }
  *{box-sizing:border-box;margin:0;padding:0}
  html,body{width:1200px;height:951px;overflow:hidden}
  body{background:var(--bg);font-family:"Montserrat",sans-serif;position:relative}
  .flyer{position:absolute;left:280px;top:60px;width:640px;height:830px;background:var(--white);overflow:hidden;box-shadow:0 10px 30px rgba(0,0,0,.25)}
  .abs{position:absolute}

  .brand{left:24px;top:24px;width:220px;height:118px;background:var(--dark);
    clip-path:polygon(0 0,100% 0,100% 62%,88% 100%,0 100%);
    color:var(--white);display:flex;flex-direction:column;justify-content:center;padding-left:22px}
  .brand-name{font-weight:800;font-size:28px;letter-spacing:1px}
  .brand-tag{font-weight:500;font-size:9.5px;letter-spacing:.6px;margin-top:4px}

  .headline{right:26px;top:28px;text-align:right;line-height:1.05}
  .headline .lead{font-weight:700;font-size:24px;color:var(--dark)}
  .headline .big{font-family:"Oswald",sans-serif;font-weight:700;font-size:34px;color:var(--orange);text-transform:uppercase}
  .headline .and{font-weight:700;font-size:26px;color:var(--dark)}

  .services{left:0;top:160px;width:262px;height:290px;background:var(--orange);padding:30px 0 0 36px;color:var(--white)}
  .services h2{font-family:"Oswald",sans-serif;font-weight:700;font-size:32px;line-height:1;text-transform:uppercase}
  .services ul{list-style:none;margin:12px 0 0 24px}
  .services li{font-weight:700;font-size:14px;line-height:24px;display:flex;align-items:center;gap:8px}
  .services svg{width:14px;height:14px}

  .hero{left:230px;top:150px;width:410px;height:270px;
    background:linear-gradient(160deg,#b9b6d6 0%,#6e6f95 45%,#3e4366 70%,#d9a25a 100%)}

  .work-panel{left:0;top:450px;width:380px;height:220px;background:var(--dark)}
  .work-photo{height:86px;width:250px;left:120px}
  .work-photo.roof{top:466px;background:linear-gradient(180deg,#9cc3e8,#5b7ea3)}
  .work-photo.plumb{top:570px;background:linear-gradient(135deg,#e4e6ea,#9ea4ab)}
  .work-label{left:40px;width:110px;height:86px;background:var(--orange);color:var(--white);
    font-weight:800;font-size:13px;line-height:1.2;text-align:center;display:flex;align-items:center;justify-content:center;text-transform:uppercase}
  .work-label.roof{top:466px}
  .work-label.plumb{top:570px}

  .promises{left:400px;top:440px;list-style:none}
  .promises li{font-weight:800;font-size:16px;color:var(--dark);line-height:28px;display:flex;align-items:center;gap:8px;text-transform:uppercase}
  .promises svg{width:16px;height:16px}
  .promise-copy{left:400px;top:560px;width:220px;font-size:10.5px;line-height:1.35;color:var(--text)}

  .cta{left:385px;top:648px;width:240px;height:70px;background:var(--orange);padding:10px 16px;color:var(--white)}
  .cta .top{font-weight:700;font-size:22px;line-height:1}
  .cta .bottom{font-weight:800;font-size:17px;color:var(--dark);margin-top:4px}
  .cta .bottom span{font-weight:700;color:var(--white)}
  .call{left:385px;top:718px;width:240px;height:70px;background:var(--dark);display:flex;align-items:center;gap:12px;padding-left:18px}
  .call svg{width:30px;height:30px}
  .call .lbl{font-weight:700;font-size:12px;color:var(--orange)}
  .call .num{font-weight:800;font-size:22px;color:var(--white)}

  .specialize{left:36px;top:690px;width:330px;line-height:1.05}
  .specialize .accent{font-weight:800;font-size:26px;color:var(--orange)}
  .specialize .main{font-weight:800;font-size:18px;color:var(--dark)}
  .specialize p{font-size:10.5px;line-height:1.35;color:var(--text);margin-top:6px}
</style>
</head>
<body>
<main class="flyer">
  <div class="abs brand">
    <span class="brand-name">HARTWELL</span>
    <span class="brand-tag">REMODELING &amp; RESTORATION</span>
  </div>

  <h1 class="abs headline">
    <span class="lead">WE ARE LICENSED</span><br>
    <span class="big">Electrical Contractor</span><br>
    <span class="and">AND </span><span class="big">Plumbers</span>
  </h1>

  <div class="abs hero" role="img" aria-label="Contractor in hard hat and tool belt standing in front of a two-storey house at dusk"></div>

  <section class="abs services">
    <h2>Our<br>Services:</h2>
    <ul>
      <li><svg viewBox="0 0 14 14"><rect x="1" y="1" width="12" height="12" fill="#fff"/><path d="M3 7l3 3 6-8" stroke="#231f20" stroke-width="2" fill="none"/></svg>ADDITION</li>
      <li><svg viewBox="0 0 14 14"><rect x="1" y="1" width="12" height="12" fill="#fff"/><path d="M3 7l3 3 6-8" stroke="#231f20" stroke-width="2" fill="none"/></svg>BASEMENTS</li>
      <li><svg viewBox="0 0 14 14"><rect x="1" y="1" width="12" height="12" fill="#fff"/><path d="M3 7l3 3 6-8" stroke="#231f20" stroke-width="2" fill="none"/></svg>KITCHENS</li>
      <li><svg viewBox="0 0 14 14"><rect x="1" y="1" width="12" height="12" fill="#fff"/><path d="M3 7l3 3 6-8" stroke="#231f20" stroke-width="2" fill="none"/></svg>BATHROOMS</li>
      <li><svg viewBox="0 0 14 14"><rect x="1" y="1" width="12" height="12" fill="#fff"/><path d="M3 7l3 3 6-8" stroke="#231f20" stroke-width="2" fill="none"/></svg>CONCRETE</li>
      <li><svg viewBox="0 0 14 14"><rect x="1" y="1" width="12" height="12" fill="#fff"/><path d="M3 7l3 3 6-8" stroke="#231f20" stroke-width="2" fill="none"/></svg>SIDING</li>
      <li><svg viewBox="0 0 14 14"><rect x="1" y="1" width="12" height="12" fill="#fff"/><path d="M3 7l3 3 6-8" stroke="#231f20" stroke-width="2" fill="none"/></svg>ROOFING</li>
    </ul>
  </section>

  <div class="abs work-panel"></div>
  <div class="abs work-photo roof" role="img" aria-label="Roofer installing metal roof panels under a blue sky"></div>
  <div class="abs work-label roof">Roof<br>Systems<br>Installed</div>
  <div class="abs work-photo plumb" role="img" aria-label="Plumber fitting a white drain pipe under a sink"></div>
  <div class="abs work-label plumb">Installed<br>Home<br>Owners</div>

  <ul class="abs promises">
    <li><svg viewBox="0 0 16 16"><path d="M2 9l4 4 8-11" stroke="#e8622c" stroke-width="3" fill="none"/></svg>Quality</li>
    <li><svg viewBox="0 0 16 16"><path d="M2 9l4 4 8-11" stroke="#e8622c" stroke-width="3" fill="none"/></svg>Always Fair Price</li>
    <li><svg viewBox="0 0 16 16"><path d="M2 9l4 4 8-11" stroke="#e8622c" stroke-width="3" fill="none"/></svg>Locally Owned</li>
    <li><svg viewBox="0 0 16 16"><path d="M2 9l4 4 8-11" stroke="#e8622c" stroke-width="3" fill="none"/></svg>100% Warranty</li>
  </ul>
  <p class="abs promise-copy">Lorem ipsum dolor sit amet, consectetuer adipiscing elit, sed diam nonummy nibh euismod tincidunt ut laoreet dolore magna aliquam erat volutpat.</p>

  <div class="abs cta">
    <div class="top">SCHEDULE A</div>
    <div class="bottom">FREE <span>INSPECTION</span></div>
  </div>
  <div class="abs call">
    <svg viewBox="0 0 30 30"><path d="M8 4c2 0 3 4 3 5s-2 2-2 3c1 3 4 6 7 7 1 0 2-2 3-2s5 1 5 3-2 5-4 5C12 25 5 18 5 8c0-2 1-4 3-4z" fill="#e8622c"/></svg>
    <div>
      <div class="lbl">CALL TODAY :</div>
      <div class="num">0987 654 321</div>
    </div>
  </div>

  <section class="abs specialize">
    <div class="accent">SPECIALIZE IN</div>
    <div class="main">ELECTRICAL CONTRACTOR<br>AND PLUMBERS</div>
    <p>Lorem ipsum dolor sit amet, consectetuer nonummy nibh euismod tincidunt ut laoreet dolore magna aliquam erat volutpat.</p>
  </section>
</main>
</body>
</html>
```